Generator Control - Superyacht Power Management System

We need a graphic design for a Touch Screen interface to control generators on Superyachts. We have a layout of the control system worked out, but need nice graphics to go with it.
The graphics comes down to a 300x460px App that i replicate several times on my 15" touchscreen as required.
See attached images.
The interface is divided up into 4 sections:
• Section#1 - 4 rectangles for the control
• Section#2 - a vertical bar graph,
• Section#3 - a section to display custom information
• Section#4 - a circuit breaker symbol.
The dimensions in pixels must be as per the attached image.
SECTION#1:
The 4 control rectangles correspond to 4 control modes:
• STOP – colours based on RED
• RUN – colours based on ORANGE
• RUN ONLINE – colours based on GREEN
• AUTO – colours based on BLUE
• THE TEXT DOESN’T HAVE TO BE ON THE GRAPHICS, WE JUST NEED THE BACKGROUND FOR THE TEXT, I ADD THE TEXT LATER USING SOFTWARE.
Each control rectangle needs to have 3 clearly identifiable states:
• Active/Selected (this is the currently active mode)
• Not Active/Not Selected (this mode is available but not currently active)
• Unavailable (this mode is not available)
SECTION#2:
The vertical bar graph design only needs the outline/frame of the bar graph. The actual moving part can be left blank; I will add that in later using an animation.
SECTION#3:
Free to look good as you want. See attached image for reference.
Within section#3 (at the top) is a 40x240px subsection, and should simply by 2 states, green or 'background colour of section#3 '. (green for when the generator is running, blend with the rest of section#3 when it is not). There are about 10 different texts I add on top of that square using software, corresponding to the status of the generator (starting, deloading, synchronizing, etc.)
SECTION#4:
Graphical representation of an electrical switch. Can be in two positions: opened or closed. See attached image as reference.

Cheif Engineers /Captains on Superyachts

Graphic Design

• Must have the same graphics style as the uploaded file#2

```html
<!DOCTYPE html>
<html lang="en">
<head>
<meta charset="utf-8">
<title>Generator Control</title>
<link rel="stylesheet" href="https://fonts.googleapis.com/css2?family=Open+Sans:wght@400;600;700&display=swap">
<style>
:root{
  --page:#efefef;
  --btn-top:#fafafa;
  --btn-bottom:#ececec;
  --btn-border:#d6d6d6;
  --off-top:#d9d9d9;
  --off-bottom:#a3a3a3;
  --off-text:#b5b5b5;
  --header:#2d3d4d;
  --header-text:#ffffff;
  --cell:#ffffff;
  --line:#e3e3e3;
  --label:#4a4a4a;
  --value:#6a6a6a;
  --green:#7cc243;
  --green-dark:#5ea52a;
  --scale:#777;
}
*{box-sizing:border-box;margin:0;padding:0}
html,body{width:1200px;height:733px;overflow:hidden}
body{background:var(--page);font-family:"Open Sans",Arial,sans-serif;position:relative}
.panel{position:absolute;top:60px;width:393px;height:613px}
.panel--offline{left:148px}
.panel--online{left:659px}
.breaker{position:absolute;left:155px;top:0;width:80px;height:131px;background:linear-gradient(#fbfbfb,#efefef);border:1px solid var(--btn-border);box-shadow:0 1px 2px rgba(0,0,0,.08);display:flex;align-items:center;justify-content:center;text-align:center;font-weight:700;font-size:14px;line-height:24px;color:#555}
.control{position:absolute;width:148px;height:93px;background:linear-gradient(var(--btn-top),var(--btn-bottom));border:1px solid var(--btn-border);box-shadow:0 1px 2px rgba(0,0,0,.1);display:flex;flex-direction:column;align-items:center;justify-content:flex-end;padding-bottom:8px;font-size:15px;color:#444}
.control svg{margin-bottom:6px}
.control--run-online{left:0;top:140px}
.control--run{left:160px;top:140px}
.control--stop{left:0;top:247px}
.control--auto{left:160px;top:247px}
.control--unavailable{background:linear-gradient(var(--off-top),var(--off-bottom));color:var(--off-text);border-color:#c4c4c4}
.control .count{color:#2a4a9a}
.status{position:absolute;left:0;top:349px;width:309px;height:50px;background:var(--header);color:var(--header-text);font-weight:700;font-size:20px;line-height:50px;padding-left:18px}
.readings{position:absolute;left:0;top:400px;width:309px;height:213px;background:var(--cell);display:grid;grid-template-columns:182px 127px}
.gauges{border-right:1px solid var(--line)}
.gauge{height:53.25px;border-bottom:1px solid var(--line);display:flex;align-items:center;padding-left:8px}
.gauge:last-child{border-bottom:none}
.gauge svg{flex:none;width:28px;margin-right:14px}
.gauge-name{font-weight:700;font-size:17px;color:var(--label);line-height:20px}
.gauge-value{font-size:16px;color:var(--value);line-height:20px;word-spacing:6px}
.electrics{display:flex;flex-direction:column}
.group{border-bottom:1px solid var(--line);padding:3px 0;display:flex;flex-direction:column;justify-content:center}
.group:last-child{border-bottom:none}
.group--volt,.group--amp{height:80px}
.group--power{flex:1}
.row{display:grid;grid-template-columns:76px 1fr;font-size:16px;color:#333;line-height:24px}
.row b{font-weight:400;text-align:right;padding-right:6px}
.row span{color:#444}
.load{position:absolute;left:315px;top:133px;width:78px;height:480px;background:#fff;border:1px solid #d2d2d2}
.load-track{position:absolute;left:0;top:0;width:41px;height:100%;background:#f4f4f4;border-right:1px solid #d2d2d2}
.load-fill{position:absolute;left:0;bottom:0;width:100%;background:repeating-linear-gradient(-55deg,var(--green) 0 12px,#8ccd55 12px 24px)}
.load-pct{position:absolute;left:0;top:0;width:100%;height:26px;background:var(--green-dark);color:#fff;font-weight:700;font-size:16px;text-align:center;line-height:26px}
.tick{position:absolute;left:41px;width:36px;border-top:1px solid #c8c8c8;font-size:11px;color:var(--scale);padding:2px 0 0 4px}
.kw{position:absolute;left:44px;bottom:2px;font-size:11px;color:var(--scale)}
</style>
</head>
<body>

<section class="panel panel--offline">
  <div class="breaker">Circuit<br>Breaker<br>Open</div>

  <div class="control control--run-online">
    <svg width="48" height="48" viewBox="0 0 48 48"><circle cx="24" cy="24" r="12" fill="#4a8ed6"/><path d="M10 22a14 14 0 0 1 26-7l3-3v11h-11l4-4a9 9 0 0 0-17 3z" fill="#6cc24a"/><path d="M38 26a14 14 0 0 1-26 7l-3 3V25h11l-4 4a9 9 0 0 0 17-3z" fill="#6cc24a"/></svg>
    Run Online
  </div>
  <div class="control control--run">
    <svg width="56" height="48" viewBox="0 0 56 48"><g fill="#f5b50f"><circle cx="21" cy="21" r="12"/><g stroke="#f5b50f" stroke-width="6"><path d="M21 4v34M4 21h34M9 9l24 24M33 9L9 33"/></g></g><circle cx="21" cy="21" r="5" fill="#fff"/><g fill="#2f7fd1"><circle cx="40" cy="34" r="8"/><g stroke="#2f7fd1" stroke-width="4"><path d="M40 23v22M29 34h22M32 26l16 16M48 26L32 42"/></g></g><circle cx="40" cy="34" r="3" fill="#fff"/></svg>
    Run
  </div>
  <div class="control control--stop">
    <svg width="48" height="48" viewBox="0 0 48 48"><circle cx="24" cy="24" r="20" fill="#d2261e"/><circle cx="24" cy="24" r="13" fill="#fff"/><path d="M14 14l20 20" stroke="#d2261e" stroke-width="6"/></svg>
    Stop
  </div>
  <div class="control control--auto">
    <svg width="50" height="48" viewBox="0 0 50 48"><path d="M8 30a18 18 0 0 1 30-20" stroke="#1f4e9a" stroke-width="3" fill="none"/><path d="M42 18a18 18 0 0 1-6 18" stroke="#d2261e" stroke-width="3" fill="none"/><circle cx="25" cy="22" r="12" fill="#4a8ed6"/><path d="M15 22h20M25 10v24" stroke="#cfe3f7" stroke-width="1.5"/><rect x="13" y="36" width="24" height="6" rx="2" fill="#333"/></svg>
    <span>Automatic <span class="count">(1)</span></span>
  </div>

  <div class="status">Running - Offline</div>

  <div class="readings">
    <div class="gauges">
      <div class="gauge">
        <svg viewBox="0 0 28 34" height="34"><rect x="10" y="2" width="8" height="22" rx="4" fill="#cfe3f5" stroke="#5a93c9"/><circle cx="14" cy="27" r="6" fill="#4a8ed6"/><rect x="12.5" y="10" width="3" height="16" fill="#4a8ed6"/></svg>
        <div><div class="gauge-name">Water Temp</div><div class="gauge-value">83 °C</div></div>
      </div>
      <div class="gauge">
        <svg viewBox="0 0 28 28" height="28"><circle cx="16" cy="14" r="10" fill="#ddd" stroke="#777" stroke-width="2"/><path d="M16 14l5-4" stroke="#333" stroke-width="2"/><path d="M5 10c-3 4-3 7 0 9 3-2 3-5 0-9z" fill="#555"/></svg>
        <div><div class="gauge-name">Oil Pressure</div><div class="gauge-value">3.8 BAR</div></div>
      </div>
      <div class="gauge">
        <svg viewBox="0 0 28 28" height="28"><circle cx="14" cy="14" r="12" fill="#3a3a3a"/><path d="M5 14a9 9 0 0 1 18 0" stroke="#c0392b" stroke-width="3" fill="none"/><path d="M14 14l6-5" stroke="#7cc243" stroke-width="2"/></svg>
        <div><div class="gauge-name">RPM</div><div class="gauge-value">1500</div></div>
      </div>
      <div class="gauge">
        <svg viewBox="0 0 28 28" height="26"><circle cx="14" cy="14" r="11" fill="none" stroke="#555" stroke-width="2.5"/><path d="M14 8v6h5" stroke="#555" stroke-width="2.5" fill="none"/></svg>
        <div><div class="gauge-name">Online Time</div><div class="gauge-value">0h 0m 0s</div></div>
      </div>
    </div>
    <div class="electrics">
      <div class="group group--volt">
        <div class="row"><b>230</b><span>VAC</span></div>
        <div class="row"><b>400</b><span>VAC</span></div>
        <div class="row"><b>50.0</b><span>HZ</span></div>
      </div>
      <div class="group group--amp">
        <div class="row"><b>0</b><span>A L1</span></div>
        <div class="row"><b>0</b><span>A L2</span></div>
        <div class="row"><b>0</b><span>A L3</span></div>
      </div>
      <div class="group group--power">
        <div class="row"><b>0</b><span>KVA</span></div>
        <div class="row"><b>0.00</b><span>PF</span></div>
      </div>
    </div>
  </div>

  <div class="load">
    <div class="load-track"></div>
    <div class="tick" style="top:0">100%</div>
    <div class="tick" style="top:96px">80%</div>
    <div class="tick" style="top:192px">60%</div>
    <div class="tick" style="top:288px">40%</div>
    <div class="tick" style="top:384px">20%</div>
    <div class="kw">0 KW</div>
  </div>
</section>

<section class="panel panel--online">
  <div class="breaker">Circuit<br>Breaker<br>Close</div>

  <div class="control control--run-online">
    <svg width="48" height="48" viewBox="0 0 48 48"><circle cx="24" cy="24" r="12" fill="#4a8ed6"/><path d="M10 22a14 14 0 0 1 26-7l3-3v11h-11l4-4a9 9 0 0 0-17 3z" fill="#6cc24a"/><path d="M38 26a14 14 0 0 1-26 7l-3 3V25h11l-4 4a9 9 0 0 0 17-3z" fill="#6cc24a"/></svg>
    Run Online
  </div>
  <div class="control control--run control--unavailable">
    <svg width="56" height="48" viewBox="0 0 56 48"><g fill="#8a8a8a"><circle cx="21" cy="21" r="12"/><g stroke="#8a8a8a" stroke-width="6"><path d="M21 4v34M4 21h34M9 9l24 24M33 9L9 33"/></g><circle cx="40" cy="34" r="8"/><g stroke="#8a8a8a" stroke-width="4"><path d="M40 23v22M29 34h22M32 26l16 16M48 26L32 42"/></g></g><circle cx="21" cy="21" r="5" fill="#bdbdbd"/><circle cx="40" cy="34" r="3" fill="#bdbdbd"/></svg>
    Run
  </div>
  <div class="control control--stop control--unavailable">
    <svg width="48" height="48" viewBox="0 0 48 48"><circle cx="24" cy="24" r="20" fill="#8c8c8c"/><circle cx="24" cy="24" r="13" fill="#b8b8b8"/><path d="M14 14l20 20" stroke="#8c8c8c" stroke-width="6"/></svg>
    Stop
  </div>
  <div class="control control--auto">
    <svg width="50" height="48" viewBox="0 0 50 48"><path d="M8 30a18 18 0 0 1 30-20" stroke="#1f4e9a" stroke-width="3" fill="none"/><path d="M42 18a18 18 0 0 1-6 18" stroke="#d2261e" stroke-width="3" fill="none"/><circle cx="25" cy="22" r="12" fill="#4a8ed6"/><path d="M15 22h20M25 10v24" stroke="#cfe3f7" stroke-width="1.5"/><rect x="13" y="36" width="24" height="6" rx="2" fill="#333"/></svg>
    <span>Automatic <span class="count">(1)</span></span>
  </div>

  <div class="status">Running - Online</div>

  <div class="readings">
    <div class="gauges">
      <div class="gauge">
        <svg viewBox="0 0 28 34" height="34"><rect x="10" y="2" width="8" height="22" rx="4" fill="#cfe3f5" stroke="#5a93c9"/><circle cx="14" cy="27" r="6" fill="#4a8ed6"/><rect x="12.5" y="10" width="3" height="16" fill="#4a8ed6"/></svg>
        <div><div class="gauge-name">Water Temp</div><div class="gauge-value">83 °C</div></div>
      </div>
      <div class="gauge">
        <svg viewBox="0 0 28 28" height="28"><circle cx="16" cy="14" r="10" fill="#ddd" stroke="#777" stroke-width="2"/><path d="M16 14l5-4" stroke="#333" stroke-width="2"/><path d="M5 10c-3 4-3 7 0 9 3-2 3-5 0-9z" fill="#555"/></svg>
        <div><div class="gauge-name">Oil Pressure</div><div class="gauge-value">3.8 BAR</div></div>
      </div>
      <div class="gauge">
        <svg viewBox="0 0 28 28" height="28"><circle cx="14" cy="14" r="12" fill="#3a3a3a"/><path d="M5 14a9 9 0 0 1 18 0" stroke="#c0392b" stroke-width="3" fill="none"/><path d="M14 14l6-5" stroke="#7cc243" stroke-width="2"/></svg>
        <div><div class="gauge-name">RPM</div><div class="gauge-value">1500</div></div>
      </div>
      <div class="gauge">
        <svg viewBox="0 0 28 28" height="26"><circle cx="14" cy="14" r="11" fill="none" stroke="#555" stroke-width="2.5"/><path d="M14 8v6h5" stroke="#555" stroke-width="2.5" fill="none"/></svg>
        <div><div class="gauge-name">Online Time</div><div class="gauge-value">0h 3m 33s</div></div>
      </div>
    </div>
    <div class="electrics">
      <div class="group group--volt">
        <div class="row"><b>230</b><span>VAC</span></div>
        <div class="row"><b>400</b><span>VAC</span></div>
        <div class="row"><b>50.0</b><span>HZ</span></div>
      </div>
      <div class="group group--amp">
        <div class="row"><b>15</b><span>A L1</span></div>
        <div class="row"><b>22</b><span>A L2</span></div>
        <div class="row"><b>19</b><span>A L3</span></div>
      </div>
      <div class="group group--power">
        <div class="row"><b>45</b><span>KVA</span></div>
        <div class="row"><b>0.00</b><span>PF</span></div>
      </div>
    </div>
  </div>

  <div class="load">
    <div class="load-track">
      <div class="load-fill" style="height:302px"><div class="load-pct">63%</div></div>
    </div>
    <div class="tick" style="top:0">100%</div>
    <div class="tick" style="top:96px">80%</div>
    <div class="tick" style="top:192px">60%</div>
    <div class="tick" style="top:288px">40%</div>
    <div class="tick" style="top:384px">20%</div>
    <div class="kw">41 KW</div>
  </div>
</section>

</body>
</html>
```